Design my dad a new business card because his current one sucks!

I need a business card designed for my fathers home maintenance business. His customers are individuals (single moms, old people etc.) as well as the occasional business. As such it needs to be accessible to both target audiences.

The front of the card should be dark grey on yellow with the logo and contain the following information:
- Warren Dobrinski
- 0487 362 914
- info@harbourlinehandyworks.com.au
- 0487 362 914

- ABN: 87 214 630 592
- 'Fully Insured'

The reverse should be yellow on dark grey and will have the web address:
- harbourlinehandyworks.com.au

And a few key services he offers:
GENERAL REPAIRS
PAINTING/TILING/
PAVING &CONCRETING
PRESSURE WASHING
ON-SITE WELDING
DECKING ADDITIONS & REPAIRS
FENCING
FULL BOND CLEANING

This will be first time the logo has been printed so you will need to come up with the best CMYK approximation of the RGB colours to make sure it is a close as possible.

```html
<!DOCTYPE html>
<html lang="en">
<head>
<meta charset="utf-8">
<title>Harbourline Handyworks – Business Card Reverse</title>
<link rel="stylesheet" href="https://fonts.googleapis.com/css2?family=Quicksand:wght@400&family=Stint+Ultra+Condensed&display=swap">
<style>
  :root {
    --page: #ffffff;
    --card: #525252;
    --accent: #f7e600;
  }
  html, body {
    margin: 0;
    padding: 0;
    width: 1200px;
    height: 900px;
    overflow: hidden;
    background: var(--page);
  }
  .canvas {
    position: relative;
    width: 1200px;
    height: 900px;
  }
  .card-reverse {
    position: absolute;
    left: 0;
    top: 128px;
    width: 1200px;
    height: 667px;
    background: var(--card);
  }
  .pointer {
    position: absolute;
    left: 0;
    top: 252px;
    width: 107px;
    height: 180px;
  }
  .web-address {
    position: absolute;
    left: 0;
    top: 84px;
    width: 1200px;
    margin: 0;
    text-align: center;
    font-family: "Quicksand", sans-serif;
    font-weight: 400;
    font-size: 46px;
    letter-spacing: 3px;
    color: var(--accent);
    line-height: 1;
  }
  .services {
    position: absolute;
    left: 145px;
    top: 262px;
    margin: 0;
    padding: 0;
    list-style: none;
    display: grid;
    grid-template-columns: 285px 305px 420px;
    grid-auto-rows: 54px;
    font-family: "Stint Ultra Condensed", sans-serif;
    font-size: 44px;
    line-height: 54px;
    color: var(--accent);
    text-transform: uppercase;
    white-space: nowrap;
  }
  .tool-icons {
    position: absolute;
    left: 296px;
    top: 585px;
    display: flex;
    gap: 44px;
  }
  .tool-icons svg {
    width: 50px;
    height: 50px;
    fill: var(--accent);
    stroke: var(--accent);
  }
</style>
</head>
<body>
<div class="canvas">
  <section class="card-reverse">
    <svg class="pointer" viewBox="0 0 107 180" aria-hidden="true">
      <polygon points="0,0 107,90 0,180" fill="var(--accent)"/>
    </svg>

    <p class="web-address">harbourlinehandyworks.com.au</p>

    <ul class="services">
      <li>General Repairs</li>
      <li>Painting/Tiling/</li>
      <li>Paving &amp;Concreting</li>
      <li>Pressure Washing</li>
      <li>On-Site Welding</li>
      <li>Decking Additions &amp; Repairs</li>
      <li>Fencing</li>
      <li>Full Bond Cleaning</li>
    </ul>

    <div class="tool-icons" aria-label="Trade tools">
      <!-- paint roller -->
      <svg viewBox="0 0 50 50" aria-label="Paint roller" role="img">
        <rect x="6" y="26" width="12" height="22" rx="2" transform="rotate(-40 12 37)" stroke="none"/>
        <path d="M20 30 L30 20 L36 22" fill="none" stroke-width="3"/>
        <rect x="34" y="4" width="6" height="20" rx="2" transform="rotate(30 37 14)" stroke="none"/>
      </svg>
      <!-- trowel -->
      <svg viewBox="0 0 50 50" aria-label="Trowel" role="img">
        <polygon points="18,22 44,6 34,34" stroke="none"/>
        <path d="M22 30 L12 40" fill="none" stroke-width="4"/>
        <rect x="4" y="38" width="10" height="6" rx="2" transform="rotate(-45 9 41)" stroke="none"/>
      </svg>
      <!-- fence -->
      <svg viewBox="0 0 50 50" aria-label="Fence" role="img">
        <polygon points="6,12 10,6 14,12 14,46 6,46" stroke="none"/>
        <polygon points="21,12 25,6 29,12 29,46 21,46" stroke="none"/>
        <polygon points="36,12 40,6 44,12 44,46 36,46" stroke="none"/>
        <rect x="4" y="18" width="42" height="5" stroke="none"/>
        <rect x="4" y="34" width="42" height="5" stroke="none"/>
      </svg>
      <!-- hammer and wrench -->
      <svg viewBox="0 0 50 50" aria-label="Hammer and wrench" role="img">
        <path d="M10 42 L38 12" fill="none" stroke-width="6" stroke-linecap="round"/>
        <path d="M10 12 L40 42" fill="none" stroke-width="6" stroke-linecap="round"/>
        <rect x="2" y="4" width="18" height="10" rx="2" transform="rotate(45 11 9)" stroke="none"/>
        <circle cx="40" cy="10" r="8" stroke="none"/>
        <circle cx="43" cy="7" r="3.5" fill="var(--card)" stroke="none"/>
      </svg>
      <!-- welding mask with sparks -->
      <svg viewBox="0 0 50 50" aria-label="Welding mask" role="img">
        <path d="M24 6 H40 Q44 6 44 12 V34 Q44 42 36 42 H28 Q24 42 24 36 Z" stroke="none"/>
        <rect x="30" y="12" width="9" height="6" fill="var(--card)" stroke="none"/>
        <path d="M10 34 L18 30 M12 24 L18 28 M6 30 L16 30 M14 40 L18 32" fill="none" stroke-width="2"/>
        <rect x="18" y="40" width="6" height="8" stroke="none"/>
      </svg>
      <!-- cleaning bucket -->
      <svg viewBox="0 0 50 50" aria-label="Cleaning bucket" role="img">
        <polygon points="8,20 42,20 38,46 12,46" stroke="none"/>
        <rect x="14" y="8" width="7" height="12" stroke="none"/>
        <rect x="28" y="6" width="8" height="14" stroke="none"/>
        <path d="M8 20 Q25 8 42 20" fill="none" stroke-width="2"/>
      </svg>
      <!-- brush -->
      <svg viewBox="0 0 50 50" aria-label="Paint brush" role="img">
        <path d="M30 20 L44 6" fill="none" stroke-width="5" stroke-linecap="round"/>
        <polygon points="24,18 32,26 28,30 20,22" stroke="none"/>
        <path d="M22 24 L6 44 M25 27 L9 46 M20 22 L4 40 M27 29 L13 47" fill="none" stroke-width="1.6"/>
      </svg>
    </div>
  </section>
</div>
</body>
</html>
```